Lawn maintenance
We are your green choice!
weekly , biweekly

Target Market(s)

lawn care

Industry/Entity Type

Lawn Care

Contact Information for Business Card

eye catching - not you normal "lawn business" card

Logo Text

Tall Oak Lawncare

Font styles to use
Serif
Sans Serif

Colors
ec1f27
00a990
9bcb3c
0455a3

Requirements
Must have
• Milo Hanford
• 410-555-0187
• Lawn maintenance
• We are your green choice!
• Call for a quote today!
• weekly or biweekly
Nice to have
• maybe some poker chips or playing cards
Should not have
• snow removal

```html
<!DOCTYPE html>
<html lang="en">
<head>
<meta charset="utf-8">
<title>Tall Oak Lawncare – Business Card</title>
<link href="https://fonts.googleapis.com/css2?family=Questrial&family=Poppins:wght@700&display=swap" rel="stylesheet">
<style>
  :root{
    --grass-light:#b8f25a;
    --grass-mid:#74d624;
    --grass-deep:#3e9a12;
    --band:#3ee27a;
    --band-soft:rgba(62,226,122,.88);
    --veil:rgba(255,255,255,.55);
    --veil-top:rgba(255,255,255,.5);
    --ink:#111;
    --brand:#3ee27a;
    --white:#fff;
  }
  *{margin:0;padding:0;box-sizing:border-box}
  html,body{width:1200px;height:724px;overflow:hidden;background:#fff}
  .card{position:relative;width:1200px;height:724px;overflow:hidden;font-family:"Questrial",sans-serif}
  .grass-photo{position:absolute;inset:0;
    background:
      radial-gradient(ellipse at 70% 0%, #d8f7a8 0%, rgba(216,247,168,0) 45%),
      linear-gradient(180deg,var(--grass-light) 0%,var(--grass-mid) 40%,var(--grass-deep) 100%);}
  .side-panel{position:absolute;left:0;top:0;width:370px;height:724px;background:var(--veil)}
  .brand{position:absolute;left:50px;top:58px;width:300px;display:flex;align-items:center;gap:14px;
    color:var(--brand);font-family:"Poppins",sans-serif;font-weight:700;font-size:34px;line-height:1.1}
  .brand-dot{flex:none;width:28px;height:28px;border-radius:50%;background:var(--brand)}
  .rule{position:absolute;left:0;top:184px;width:370px;height:15px;background:var(--band)}
  .name{position:absolute;left:32px;top:216px;font-size:49px;color:var(--ink);letter-spacing:-.5px;white-space:nowrap}
  .phone{position:absolute;left:0;top:289px;width:370px;height:59px;background:var(--band);
    color:var(--white);font-size:36px;display:flex;align-items:center;justify-content:flex-end;padding-right:26px;white-space:nowrap}
  .title-band{position:absolute;left:370px;top:94px;width:824px;height:104px;background:var(--veil-top);
    display:flex;align-items:center;justify-content:flex-end;padding-right:32px;color:var(--band);font-size:62px}
  .phone-icon{position:absolute;left:370px;top:264px;width:61px;height:62px;background:var(--band);
    display:flex;align-items:center;justify-content:center}
  .tag{position:absolute;height:60px;background:var(--band-soft);color:var(--white);font-size:42px;
    display:inline-flex;align-items:center;white-space:nowrap;padding:0 18px 0 14px}
  .tag-service{right:36px;top:394px;padding-right:20px}
  .tag-slogan{left:370px;top:464px;height:58px;padding-left:12px}
  .tag-cta{right:6px;top:531px;padding-right:14px}
  .tag-schedule{left:370px;top:598px;height:63px;padding-left:12px;padding-right:60px}
</style>
</head>
<body>
<div class="card">
  <div class="grass-photo" role="img" aria-label="Close-up photograph of bright green grass blades"></div>
  <div class="side-panel"></div>

  <div class="brand"><span class="brand-dot"></span><span>Tall Oak Lawncare</span></div>
  <div class="rule"></div>
  <div class="name">Milo Hanford</div>
  <div class="phone">410-555-0187</div>

  <div class="title-band">Lawn Care</div>
  <div class="phone-icon">
    <svg width="22" height="38" viewBox="0 0 22 38" aria-hidden="true">
      <rect x="1.5" y="1.5" width="19" height="35" rx="3" fill="none" stroke="#fff" stroke-width="2.5"/>
      <line x1="1.5" y1="7" x2="20.5" y2="7" stroke="#fff" stroke-width="2"/>
      <line x1="1.5" y1="30" x2="20.5" y2="30" stroke="#fff" stroke-width="2"/>
      <circle cx="11" cy="33.3" r="1.4" fill="#fff"/>
    </svg>
  </div>

  <div class="tag tag-service">Lawn Maintenance</div>
  <div class="tag tag-slogan">We Are Your Green Choice!</div>
  <div class="tag tag-cta">Call For A Quote Today!</div>
  <div class="tag tag-schedule">Weekly Or Biweekly</div>
</div>
</body>
</html>
```